Flayer Elektrofirma
Zielgruppe
Elektrotechnik Vollmar ist Ihr Partner in den Bereichen Elektroinstallation, Netzwerktechnik, Satelitentechnik und Telefon / ISDN Anlagen.
Aufgabenstellung
Ich brauche für meine Existenzgründung einen D5 Flyer, Vorder und Rückseite.
Auf dem Flyer sollte mindestens vorhanden sein:
- Firmenname (Elektrotechnik)
- Betriebsgründer
- Logo (Das grüne)
- Ein Foto von mir
- Text in rot (24h am Tag für Sie erreichbar)
- Aufgabenbereiche (Elektroinstallation, Netzwerktechnik, Telefonanlagen, Service Photovoltaik, Solare Datensysteme.
- Telefonnummer
- Webseitenadresse
- Ein Text wie ( Existenzgründung bla bla bla, möchten wir uns vorstellen bla bla bla)
Gerne dürfen Fotos und Texte aus meiner Webseite verwendet werden.
Als Schriftarten bitte nur Arial und Neuropolitical verwenden.
Ich lade das Logo hoch, wenn noch was benötigt wird bitte einfach melden.
Für mein eigenes Foto bitte einen Platzhalter lassen, ich muss noch ein Foto erstellen lassen.

```html
<!DOCTYPE html>
<html lang="de">
<head>
<meta charset="utf-8">
<title>Elektrotechnik Vollmar – Flyer Vorder- und Rückseite</title>
<link rel="stylesheet" href="https://fonts.googleapis.com/css2?family=Arimo:wght@400;700&family=Michroma&display=swap">
<style>
  :root {
    --green: #8fbf2a;
    --slate: #46515c;
    --red: #c3151c;
    --ink: #2b2f33;
    --paper: #ffffff;
    --backdrop: #e4e6e8;
    --soft: #f1f2f3;
    --display: "Michroma", sans-serif;
    --body: "Arimo", Arial, sans-serif;
  }
  * { box-sizing: border-box; margin: 0; padding: 0; }
  html, body { width: 1200px; height: 1200px; overflow: hidden; }
  body { background: var(--backdrop); font-family: var(--body); color: var(--ink); position: relative; }

  .flyer { position: absolute; width: 760px; height: 520px; background: var(--paper); overflow: hidden; box-shadow: 0 6px 18px rgba(0,0,0,.18); }
  .flyer--front { left: 50px; top: 50px; }
  .flyer--back { left: 390px; top: 630px; }

  .brand { position: absolute; display: flex; align-items: center; gap: 14px; }
  .brand__dot { width: 62px; height: 62px; border-radius: 50%; background: var(--green); flex: none; }
  .brand__name { font-family: var(--display); color: var(--green); font-size: 30px; line-height: 1.15; letter-spacing: 1px; }

  /* Front */
  .flyer--front .brand { left: 40px; top: 36px; }
  .front__photo { position: absolute; right: 0; top: 0; width: 420px; height: 430px;
    background: radial-gradient(ellipse at 55% 45%, #9a8f86 0%, #c9c5c1 38%, #eeeeee 70%, #ffffff 100%); }
  .services { position: absolute; left: 44px; top: 150px; }
  .services__title { font-family: var(--display); color: var(--green); font-size: 19px; line-height: 1.45; margin-bottom: 14px; }
  .services__list { list-style: none; }
  .services__item { display: flex; align-items: center; gap: 10px; font-weight: 700; font-size: 19px; color: var(--ink); margin-bottom: 8px; }
  .services__item svg { flex: none; }
  .front__claim { position: absolute; left: 0; bottom: 0; width: 100%; height: 90px; background: var(--slate);
    color: #fff; font-weight: 700; font-size: 26px; display: flex; align-items: center; justify-content: center; }
  .front__claim em { font-style: normal; color: var(--green); margin: 0 8px; }

  /* Back */
  .flyer--back .brand { left: 40px; top: 22px; }
  .availability { position: absolute; left: 420px; top: 34px; width: 180px; padding: 9px 10px; background: var(--red); color: #fff;
    font-weight: 700; font-size: 16px; line-height: 1.3; text-align: center; box-shadow: 0 3px 6px rgba(0,0,0,.25); }
  .owner-photo { position: absolute; right: 0; top: 0; width: 130px; height: 114px;
    background: linear-gradient(160deg, #d8c2ac 0%, #eee4da 55%, #ffffff 100%); }
  .contact-bar { position: absolute; left: 0; top: 114px; width: 100%; height: 38px; background: var(--slate); color: #fff;
    display: flex; justify-content: space-between; align-items: center; padding: 0 36px; font-size: 14px; }
  .contact-bar span b { font-weight: 400; color: var(--green); }
  .back__body { position: absolute; left: 0; top: 152px; width: 100%; height: 300px; background: linear-gradient(#fff, var(--soft)); }

  .business-card { position: absolute; left: 30px; top: 172px; width: 150px; height: 262px; background: #fff; box-shadow: 0 2px 8px rgba(0,0,0,.22); overflow: hidden; }
  .business-card__inner { position: absolute; width: 262px; height: 150px; left: 150px; top: 0; transform-origin: 0 0; transform: rotate(90deg); padding: 12px 14px; font-size: 7px; line-height: 1.35; }
  .business-card__name { font-family: var(--display); color: var(--green); font-size: 10px; margin-bottom: 28px; }
  .business-card__person { font-size: 10px; font-weight: 700; color: var(--ink); }
  .business-card__cols { display: flex; gap: 14px; margin-top: 6px; }
  .business-card__hot { color: var(--red); }

  .columns { position: absolute; left: 208px; top: 172px; width: 520px; display: grid; grid-template-columns: 1fr 1fr; column-gap: 26px; }
  .topic { margin-bottom: 14px; }
  .topic__title { font-family: var(--display); color: var(--green); font-size: 11px; line-height: 1.35; margin-bottom: 6px; }
  .topic__text { font-size: 8.6px; line-height: 1.4; color: var(--ink); }

  .owner-bar { position: absolute; left: 0; bottom: 0; width: 100%; height: 62px; background: #e7e8e9; display: flex; align-items: center; justify-content: flex-end; padding-right: 40px; font-size: 16px; color: var(--ink); }
</style>
</head>
<body>

<section class="flyer flyer--front" aria-label="Flyer Vorderseite">
  <div class="front__photo" role="img" aria-label="Foto: Mann mit elektrisch aufgestellten Haaren hält zerrissene Kabel"></div>
  <div class="brand">
    <span class="brand__dot"></span>
    <span class="brand__name">Vollmar<br>Elektrotechnik</span>
  </div>
  <div class="services">
    <h2 class="services__title">Ihr Partner<br>in den Bereichen</h2>
    <ul class="services__list">
      <li class="services__item"><svg width="14" height="14" viewBox="0 0 14 14"><path d="M1 7.5 L5 11.5 L13 2" fill="none" stroke="#8fbf2a" stroke-width="2.4"/></svg>Elektroinstallation</li>
      <li class="services__item"><svg width="14" height="14" viewBox="0 0 14 14"><path d="M1 7.5 L5 11.5 L13 2" fill="none" stroke="#8fbf2a" stroke-width="2.4"/></svg>Netzwerktechnik</li>
      <li class="services__item"><svg width="14" height="14" viewBox="0 0 14 14"><path d="M1 7.5 L5 11.5 L13 2" fill="none" stroke="#8fbf2a" stroke-width="2.4"/></svg>Telefonanlagen</li>
      <li class="services__item"><svg width="14" height="14" viewBox="0 0 14 14"><path d="M1 7.5 L5 11.5 L13 2" fill="none" stroke="#8fbf2a" stroke-width="2.4"/></svg>Service Photovoltaik</li>
      <li class="services__item"><svg width="14" height="14" viewBox="0 0 14 14"><path d="M1 7.5 L5 11.5 L13 2" fill="none" stroke="#8fbf2a" stroke-width="2.4"/></svg>Solare Datensysteme</li>
    </ul>
  </div>
  <p class="front__claim">Lassen Sie das lieber von einem <em>Fachmann</em> machen!</p>
</section>

<section class="flyer flyer--back" aria-label="Flyer Rückseite">
  <div class="brand">
    <span class="brand__dot"></span>
    <span class="brand__name">Vollmar<br>Elektrotechnik</span>
  </div>
  <p class="availability">24 Stunden am Tag<br>für Sie erreichbar!</p>
  <div class="owner-photo" role="img" aria-label="Platzhalter für Porträtfoto des Inhabers"></div>
  <div class="contact-bar">
    <span>Telefon <b>+49 8031-552 19 30</b></span>
    <span>Email <b>info@elektriker-vollmar.de</b></span>
    <span>Web <b>www.elektriker-vollmar.de</b></span>
  </div>
  <div class="back__body"></div>

  <div class="business-card" aria-label="Visitenkarte">
    <div class="business-card__inner">
      <p class="business-card__name">Vollmar Elektrotechnik</p>
      <p class="business-card__person">Markus Vollmar</p>
      <p>Elektromeister für Energie und Gebäudetechnik</p>
      <div class="business-card__cols">
        <p>Elektrotechnik Vollmar<br>Lindenstraße 12, 83059 Kolbermoor<br><span class="business-card__hot">24 Stunden am Tag für Sie erreichbar</span></p>
        <p>Tel +49 8031 / 552 19 30<br>Fax +49 8031 / 552 19 31<br>www.elektriker-vollmar.de</p>
      </div>
    </div>
  </div>

  <div class="columns">
    <div>
      <article class="topic">
        <h3 class="topic__title">Energie- und<br>Gebäudetechnik</h3>
        <p class="topic__text">Elektrotechnik Vollmar, Ihr kompetenter Partner für moderne Elektroinstallation und Elektroplanung in den Bereichen Neubau und Altbaurenovierung. Eine ausführliche Beratung, genaue Planung und fachgerechte Installation gehören zu unseren täglichen Aufgaben. Wir sind Ihr Partner vor Ort um jederzeit individuelle und persönlich auf Sie zugeschnittene Lösungen zu finden.</p>
      </article>
      <article class="topic">
        <h3 class="topic__title">Netzwerktechnik</h3>
        <p class="topic__text">Wenn Sie Netzwerktechnik von morgen wollen und keine Lösungen, die heute schon von gestern sind, vertrauen Sie unserer Erfahrung. EDV-gestützte Organisations- und Arbeitshilfen sind heute in fast allen Branchen unverzichtbarer Bestandteil erfolgreicher Betriebskonzepte und Voraussetzung für zeitgemäße Bürokommunikation.</p>
      </article>
    </div>
    <div>
      <article class="topic">
        <h3 class="topic__title">Solare<br>Datensysteme</h3>
        <p class="topic__text">Wir bieten Ihnen modernste Monitoring-Systeme mit umfangreicher und professioneller Auswertungssoftware, die jederzeit per PC, Tablet oder Handy erreichbar ist. Das intelligente Monitoring-System sammelt alle Daten Ihrer PV-Anlage, wertet diese aus und informiert Sie mit zahlreichen Zusatzdienstleistungen per E-Mail oder SMS über mögliche Störungen oder drohende Ertragsausfälle.</p>
      </article>
      <article class="topic">
        <h3 class="topic__title">Telefon- und ISDN-Anlagen</h3>
        <p class="topic__text">Ob Analog, ISDN oder moderne DSL-Technik, der Bereich der Telekommunikation steht und stand in den letzten Jahren in einem starken Wandel. Was sie auch benötigen, wir erarbeiten zusammen mit Ihnen maßgeschneiderte Lösungen für Ihre Bedürfnisse.</p>
      </article>
    </div>
  </div>

  <p class="owner-bar">Inhaber: Markus Vollmar · Lindenstraße 12 · 83059 Kolbermoor</p>
</section>

</body>
</html>
```